Mental Health care Company in Washington DC

We are a new mental health care services provider in Washington DC. Please look at these sites.
https://marlowbrookpartners.com
https://www.quillstoneinc.com
https://velmarsh-kt.org/
https://www.trivanqx.com
https://www.thelanternofqz.com

```html
<!DOCTYPE html>
<html lang="en">
<head>
<meta charset="utf-8">
<title>Elmwood Health – Mental Health Care</title>
<link href="https://fonts.googleapis.com/css2?family=Poppins:wght@200;300;400;500;600;700;800&display=swap" rel="stylesheet">
<style>
:root{
  --orange:#e07b2c;
  --orange-soft:#f4a766;
  --peach:#fbd9bd;
  --teal:#9fd9dc;
  --teal-deep:#5fbcc2;
  --navy:#0f1a3d;
  --ink:#3a3f4f;
  --muted:#6b7080;
  --line:#d9dbe0;
  --cream:#fbf1e8;
  --white:#ffffff;
}
*{margin:0;padding:0;box-sizing:border-box}
html,body{width:1200px;height:4431px;overflow:hidden}
body{position:relative;font-family:'Poppins',sans-serif;color:var(--ink);background:var(--white)}
.abs{position:absolute}
svg{display:block}

/* top bar */
.topbar{left:0;top:0;width:1200px;height:24px;display:flex;font-size:11px;color:#fff}
.topbar .hours{width:608px;background:var(--orange);display:flex;align-items:center;justify-content:center;gap:6px}
.topbar .help{flex:1;background:var(--teal-deep);display:flex;align-items:center;justify-content:center;gap:6px;color:var(--navy)}

/* header */
.header{left:0;top:24px;width:1200px;height:54px;border-bottom:1px solid var(--line)}
.search{left:228px;top:13px;width:232px;height:28px;border:1px solid var(--line);border-radius:14px;font-size:11px;padding:6px 14px;color:var(--navy)}
.search .dot{position:absolute;right:5px;top:5px;width:17px;height:17px;border-radius:50%;background:var(--orange)}
.brand{left:0;width:1200px;top:10px;text-align:center;font-size:25px;font-weight:500;color:var(--navy);letter-spacing:-.5px}
.socials{left:900px;top:14px;display:flex;gap:6px}
.socials span{width:26px;height:26px;border:1px solid var(--navy);border-radius:50%}
.nav{left:0;top:78px;width:1200px;height:35px;display:flex;justify-content:center;align-items:center;gap:16px;font-size:11px;font-weight:500;color:var(--navy)}
.nav .sep{color:var(--orange);font-size:14px}

/* hero */
.hero{left:0;top:113px;width:1200px;height:470px;background:linear-gradient(90deg,#d9812f 0%,#c98a40 35%,#8f955c 65%,#6f8b5c 100%)}
.hero-photo{left:560px;top:0;width:640px;height:470px;background:radial-gradient(ellipse at 55% 50%,#c9a58a 0%,#9a8c6a 45%,rgba(111,139,92,0) 75%)}
.hero h1{left:150px;top:70px;color:#fff;font-size:65px;line-height:67px;font-weight:200}
.hero h1 b{font-weight:800;display:block}
.hero .lead{left:150px;top:286px;width:340px;padding-left:10px;border-left:3px solid #fff;color:#fff;font-size:12px;line-height:18px}
.btn{display:inline-flex;align-items:center;gap:10px;height:34px;border-radius:17px;padding:0 5px 0 18px;font-size:11px;font-weight:500;color:#fff}
.btn i{width:25px;height:25px;border-radius:50%;background:#fff;display:flex;align-items:center;justify-content:center}
.hero .b1{left:150px;top:343px;background:var(--teal)}
.hero .b2{left:279px;top:343px;background:var(--orange)}
.dots{left:1023px;top:192px;display:flex;flex-direction:column;gap:8px}
.dots span{width:22px;height:22px;border-radius:50%;border:1px solid rgba(255,255,255,.7);color:#fff;font-size:9px;display:flex;align-items:center;justify-content:center}
.tear{left:0;width:1200px}
.scroll-btn{left:581px;top:555px;width:38px;height:38px;border-radius:50%;background:#fff;box-shadow:0 3px 10px rgba(0,0,0,.15);display:flex;align-items:center;justify-content:center}

/* about */
.about{left:0;top:583px;width:1200px;height:552px;background:var(--teal)}
.about .img1{left:189px;top:122px;width:181px;height:353px;border-radius:90px 0 90px 90px/90px 0 120px 120px;background:linear-gradient(170deg,#e7e4df,#9da2a4 70%,#6f7478)}
.about .img2{left:382px;top:65px;width:182px;height:281px;border-radius:91px 91px 0 0;background:linear-gradient(170deg,#d8cfc6,#8e8076 60%,#5d6066)}
.about .o1{left:284px;top:122px;width:86px;height:47px;background:var(--orange);border-radius:40px 0 0 0}
.about .o2{left:382px;top:346px;width:130px;height:74px;background:var(--orange);border-radius:0 0 70px 70px/0 0 74px 74px}
.kicker{font-size:10px;font-weight:500;color:var(--orange);letter-spacing:.5px;display:flex;align-items:center;gap:6px}
.kicker::after,.kicker.c::before{content:"";width:26px;height:1px;background:var(--orange)}
.about .kicker{left:619px;top:85px}
.about h2{left:619px;top:98px;font-size:44px;line-height:46px;font-weight:200;color:var(--navy)}
.about h2 b{display:block;font-weight:800;font-size:44px}
.about .txt{left:619px;top:246px;width:410px;font-size:11px;line-height:18px;color:var(--ink)}
.ticks{font-size:11px;font-weight:500;color:var(--navy)}
.ticks li{list-style:none;display:flex;align-items:center;gap:6px;height:28px}
.about .ticks{left:619px;top:359px}
.about .btn{left:619px;top:430px;background:var(--orange)}

/* common headings */
.center{left:0;width:1200px;text-align:center}
.sec-title{font-size:46px;line-height:46px;font-weight:200;color:var(--navy)}
.sec-title b{font-weight:800}
.kicker.c{justify-content:center}

/* services */
.svc-desc{font-size:12px;line-height:18px;color:var(--ink)}
.card{top:1347px;width:287px}
.card .pic{height:193px;border-radius:0 28px 0 44px}
.card .plus{position:absolute;left:123px;top:168px}
.card h3{position:absolute;left:10px;top:228px;font-size:18px;font-weight:700;color:var(--teal-deep);opacity:.95}
.card .num{position:absolute;right:0;top:220px;font-size:50px;font-weight:700;color:#d6eff0;line-height:50px}
.card p{position:absolute;left:10px;top:261px;width:250px;font-size:11px;line-height:18px}
.card .rule{position:absolute;left:10px;top:325px;width:277px;height:2px;background:var(--line)}
.card .more{position:absolute;left:10px;top:347px;font-size:11px;font-weight:500;color:var(--navy)}
.card .go{position:absolute;right:0;top:341px;width:26px;height:26px;border-radius:50%;background:var(--orange-soft);display:flex;align-items:center;justify-content:center}

/* ready */
.ready{left:0;top:1832px;width:1200px;height:680px;background:linear-gradient(180deg,#fff 0%,#fff 35%,#fde3cb 65%,#f6a868 100%)}
.ready h2{left:160px;top:42px;font-size:44px;line-height:44px;font-weight:200;color:var(--navy);z-index:2}
.ready h2 b{font-weight:800;display:block}
.ready .txt{left:160px;top:188px;width:330px;font-size:11px;line-height:19px;z-index:2}
.ready .ticks{left:767px;top:44px;font-size:14px;font-weight:400;color:var(--ink)}
.ready .ticks li{height:36px;gap:10px}
.cross-v{left:552px;top:108px;width:140px;height:280px;background:var(--teal);border-radius:70px 70px 0 0}
.cross-h{left:692px;top:280px;width:232px;height:135px;background:var(--teal);border-radius:0 60px 60px 0}
.cross-o{left:318px;top:335px;width:210px;height:130px;background:var(--orange);border-radius:60px 0 0 60px}
.people{left:510px;top:190px;width:360px;height:490px;border-radius:180px 180px 0 0;background:linear-gradient(170deg,#e8c8b0 0%,#b28c74 40%,#4f5f7e 80%,#3b4a68 100%)}

/* testimonials */
.tcard{top:2718px;width:421px;height:275px;background:#fff;border-radius:130px 30px 40px 130px/110px 30px 40px 110px;box-shadow:0 8px 24px rgba(0,0,0,.08)}
.tcard .q{position:absolute;left:68px;top:-6px;width:36px;height:36px;border-radius:50%;background:var(--orange-soft);color:#fff;font-weight:800;font-size:22px;display:flex;align-items:center;justify-content:center}
.tcard p{position:absolute;left:58px;top:56px;width:270px;text-align:center;font-size:11px;line-height:18px;color:var(--ink)}
.tcard .who{position:absolute;left:58px;top:196px;width:270px;text-align:center;font-size:11px;color:var(--ink)}
.tcard .who b{display:block;font-weight:600;color:var(--navy)}
.tcard .av{position:absolute;right:10px;bottom:-20px;width:76px;height:76px;border-radius:50%;border:4px solid #fff;background:linear-gradient(160deg,#c88a6a,#7a3a2e)}

/* blogs */
.blogs{left:0;top:3130px;width:1200px;height:700px;background:var(--teal)}
.bcard{top:215px;width:290px}
.bcard .pic{height:362px;border-radius:145px 145px 0 0}
.bcard .plus{position:absolute;left:6px;top:296px;width:68px;height:68px;border-radius:50%;background:var(--orange-soft);display:flex;align-items:center;justify-content:center;border:4px solid rgba(255,255,255,.5)}
.bcard h3{margin-top:16px;padding-left:26px;font-size:13px;line-height:21px;font-weight:700;color:var(--navy)}

/* partners */
.plogo{top:3956px;width:172px;height:60px;border:1px solid var(--line);border-radius:0 22px 0 22px;display:flex;align-items:center;justify-content:center}
.plogo span{width:90px;height:22px;border-radius:11px;background:#e7e9ee}

/* footer */
.footer{left:0;top:4085px;width:1200px;height:346px;background:var(--cream)}
.footer .brand2{left:164px;top:78px;font-size:30px;font-weight:500;color:var(--navy)}
.footer .about-txt{left:164px;top:128px;width:300px;font-size:11px;line-height:17px;color:var(--ink)}
.footer h4{font-size:19px;font-weight:600;color:var(--navy);letter-spacing:.5px}
.links li,.contact li{list-style:none;display:flex;gap:8px;font-size:11px;color:var(--ink);line-height:15px}
.links li{height:27px}
.contact li{margin-bottom:14px}
.caret{color:var(--orange);font-weight:700}
.copy{left:150px;top:284px;width:900px;border-top:1px solid var(--line);padding-top:12px;text-align:center;font-size:11px;color:var(--ink)}
</style>
</head>
<body>

<div class="abs topbar">
  <div class="hours"><svg width="11" height="11" viewBox="0 0 12 12"><circle cx="6" cy="6" r="5" fill="none" stroke="#fff"/><path d="M6 3v3l2 1" stroke="#fff" fill="none"/></svg>HOURS: M-F 8:30 A.M. – 5:00 P.M.</div>
  <div class="help"><svg width="11" height="11" viewBox="0 0 12 12"><path d="M2 1h3l1 3-2 1a7 7 0 0 0 3 3l1-2 3 1v3c-6 0-10-4-10-9z" fill="#0f1a3d"/></svg>24/7 HELP 041 552 3870</div>
</div>

<header class="abs header">
  <div class="abs search">Search...<span class="dot"></span></div>
  <div class="abs brand">Elmwood Health</div>
  <div class="abs socials"><span></span><span></span><span></span></div>
</header>
<nav class="abs nav">
  <span>HOME</span><span class="sep">✣</span><span>ABOUT US</span><span class="sep">✣</span><span>OUR SERVICES</span><span class="sep">✣</span><span>NEWS &amp; EVENTS</span><span class="sep">✣</span><span>CONTACT US</span>
</nav>

<section class="abs hero">
  <div class="abs hero-photo" role="img" aria-label="Photo of a laughing young couple, the woman riding on the man's back outdoors"></div>
  <h1 class="abs">Help Your<b>Best Mental</b><b>Health</b></h1>
  <p class="abs lead">We provide each individual with assistance to help them lead better and happier lives.</p>
  <a class="abs btn b1">Read More <i><svg width="10" height="10" viewBox="0 0 10 10"><path d="M2 8L8 2M3 2h5v5" stroke="#0f1a3d" fill="none" stroke-width="1.4"/></svg></i></a>
  <a class="abs btn b2">Make an Appointment <i><svg width="10" height="10" viewBox="0 0 10 10"><path d="M2 8L8 2M3 2h5v5" stroke="#e07b2c" fill="none" stroke-width="1.4"/></svg></i></a>
  <div class="abs dots"><span>1</span><span>2</span><span>3</span></div>
  <svg class="abs" style="left:1026px;top:360px" width="16" height="60" viewBox="0 0 16 60"><path d="M8 0v58M1 50l7 8 7-8" stroke="#fff" fill="none" stroke-width="1.5"/></svg>
</section>
<svg class="abs tear" style="top:560px" width="1200" height="30" viewBox="0 0 1200 30" preserveAspectRatio="none"><path d="M0 18 L60 12 L120 20 L190 10 L260 19 L330 11 L400 21 L470 13 L540 20 L610 9 L680 19 L750 12 L820 20 L890 10 L960 18 L1030 11 L1100 20 L1160 13 L1200 17 L1200 30 L0 30Z" fill="#9fd9dc"/></svg>
<div class="abs scroll-btn"><svg width="14" height="14" viewBox="0 0 14 14"><path d="M3 3l4 4 4-4M3 7l4 4 4-4" stroke="#0f1a3d" fill="none" stroke-width="1.4"/></svg></div>

<section class="abs about">
  <div class="abs o1"></div>
  <div class="abs img1" role="img" aria-label="Photo of a woman sitting on a sofa, head in hand, beside a laptop"></div>
  <div class="abs img2" role="img" aria-label="Photo of a therapist holding a client's hands in a session"></div>
  <div class="abs o2"></div>
  <div class="abs kicker">WELCOME TO</div>
  <h2 class="abs">About<b>Elmwood Mental</b><b>Services</b></h2>
  <p class="abs txt">Along with the development of social life, people today encounter many strange and difficult diseases. Here we want to mention mental health disease, can be understood as a major problem of human beings in modern society but has not been paid attention. We help your body restore itself by harnessing your own healing potential with a variety of techniques to combat areas of disease.</p>
  <ul class="abs ticks">
    <li><svg width="16" height="16" viewBox="0 0 16 16"><path d="M8 1v5M8 10v5M1 8h5M10 8h5" stroke="#e07b2c" stroke-width="3" stroke-linecap="round"/></svg>All reports for clients are made simple and easy to understand</li>
    <li><svg width="16" height="16" viewBox="0 0 16 16"><path d="M8 1v5M8 10v5M1 8h5M10 8h5" stroke="#e07b2c" stroke-width="3" stroke-linecap="round"/></svg>User- friendly website offers custom settings for each physician</li>
  </ul>
  <a class="abs btn">Read More <i><svg width="10" height="10" viewBox="0 0 10 10"><path d="M2 8L8 2M3 2h5v5" stroke="#e07b2c" fill="none" stroke-width="1.4"/></svg></i></a>
</section>

<div class="abs center kicker c" style="top:1200px">SERVICES</div>
<h2 class="abs center sec-title" style="top:1222px">Our <b>Services</b></h2>
<p class="abs center svc-desc" style="top:1278px">Our goal is to provide customers with the best service, for us to help<br>customers overcome their barriers is a noble task</p>

<div class="abs card" style="left:150px">
  <div class="pic" role="img" aria-label="Photo of a man in a therapy session with a counsellor" style="background:linear-gradient(135deg,#e9d2be,#c99a78 60%,#f2c9a4)"></div>
  <svg class="plus" width="44" height="50" viewBox="0 0 44 50"><path d="M16 0h12v19h16v12H28v19H16V31H0V19h16z" fill="#9fd9dc"/></svg>
  <h3>Depression Therapy</h3><div class="num">01</div>
  <p>Sed ut perspiciatis unde omnis iste natus error sit voluptatem accusant doloremqe laudantium.</p>
  <div class="rule"></div><div class="more">Read More</div>
  <div class="go"><svg width="10" height="10" viewBox="0 0 10 10"><path d="M2 8L8 2M3 2h5v5" stroke="#fff" fill="none" stroke-width="1.4"/></svg></div>
</div>
<div class="abs card" style="left:458px">
  <div class="pic" role="img" aria-label="Photo of a couple in a counselling session" style="background:linear-gradient(135deg,#ead6c4,#c08a66 60%,#f0c39c)"></div>
  <svg class="plus" width="44" height="50" viewBox="0 0 44 50"><path d="M16 0h12v19h16v12H28v19H16V31H0V19h16z" fill="#9fd9dc"/></svg>
  <h3 style="color:#ef9a55">Couples Counseling</h3><div class="num">02</div>
  <p>Sed ut perspiciatis unde omnis iste natus error sit voluptatem accusant doloremqe laudantium.</p>
  <div class="rule"></div><div class="more">Read More</div>
  <div class="go"><svg width="10" height="10" viewBox="0 0 10 10"><path d="M2 8L8 2M3 2h5v5" stroke="#fff" fill="none" stroke-width="1.4"/></svg></div>
</div>
<div class="abs card" style="left:766px">
  <div class="pic" role="img" aria-label="Photo of a happy couple outdoors in the city" style="background:linear-gradient(135deg,#e3e0dc,#c7a88e 55%,#f3c29b)"></div>
  <svg class="plus" width="44" height="50" viewBox="0 0 44 50"><path d="M16 0h12v19h16v12H28v19H16V31H0V19h16z" fill="#9fd9dc"/></svg>
  <h3>Relationships</h3><div class="num">03</div>
  <p>Sed ut perspiciatis unde omnis iste natus error sit voluptatem accusant doloremqe laudantium.</p>
  <div class="rule"></div><div class="more">Read More</div>
  <div class="go"><svg width="10" height="10" viewBox="0 0 10 10"><path d="M2 8L8 2M3 2h5v5" stroke="#fff" fill="none" stroke-width="1.4"/></svg></div>
</div>
<svg class="abs" style="left:550px;top:1772px" width="100" height="38" viewBox="0 0 100 38"><circle cx="35" cy="19" r="18" fill="none" stroke="#0f1a3d"/><circle cx="65" cy="19" r="18" fill="none" stroke="#0f1a3d"/><path d="M2 19h40M8 13l-6 6 6 6M58 19h40M92 13l6 6-6 6" stroke="#5fbcc2" fill="none" stroke-width="1.4"/></svg>

<section class="abs ready">
  <div class="abs cross-v"></div>
  <div class="abs cross-h"></div>
  <div class="abs cross-o"></div>
  <div class="abs people" role="img" aria-label="Photo of a woman comforting a worried young woman seated on a chair"></div>
  <h2 class="abs">We are always<b>ready for every</b><b>People</b></h2>
  <p class="abs txt">Our goal is to help our customers be satisfied and solve problems when leaving, we are not seeking profits that we want to share, sympathize, help you solve your worries and troubles.</p>
  <ul class="abs ticks">
    <li><svg width="18" height="18" viewBox="0 0 16 16"><path d="M8 1v5M8 10v5M1 8h5M10 8h5" stroke="#e07b2c" stroke-width="3" stroke-linecap="round"/></svg>Cheap Price And Quality</li>
    <li><svg width="18" height="18" viewBox="0 0 16 16"><path d="M8 1v5M8 10v5M1 8h5M10 8h5" stroke="#e07b2c" stroke-width="3" stroke-linecap="round"/></svg>Professional Team</li>
    <li><svg width="18" height="18" viewBox="0 0 16 16"><path d="M8 1v5M8 10v5M1 8h5M10 8h5" stroke="#e07b2c" stroke-width="3" stroke-linecap="round"/></svg>Years Of Experience</li>
    <li><svg width="18" height="18" viewBox="0 0 16 16"><path d="M8 1v5M8 10v5M1 8h5M10 8h5" stroke="#e07b2c" stroke-width="3" stroke-linecap="round"/></svg>Dedicated Support</li>
  </ul>
</section>
<svg class="abs tear" style="top:2500px" width="1200" height="22" viewBox="0 0 1200 22" preserveAspectRatio="none"><path d="M0 10 L70 4 L140 12 L210 5 L280 13 L350 6 L420 12 L490 4 L560 11 L630 5 L700 13 L770 6 L840 12 L910 4 L980 11 L1050 5 L1120 12 L1200 6 L1200 22 L0 22Z" fill="#fff"/></svg>

<div class="abs center kicker c" style="top:2570px">TESTIMONIALS</div>
<h2 class="abs center sec-title" style="top:2594px">What <b>Our</b><br><b>Clients Says</b></h2>

<div class="abs tcard" style="left:172px">
  <div class="q">❝</div>
  <p>Sed a euismod turpis. Donec ullamcorper digni ssim suscipit. Quisque libero tortor, tempus et egestas sit amet, porttitor et dolor. Aenean ultri cies imperdiet velit ut finibus. Suspendisse sit amet massa orci. Morbi pellentesque eros quis lacinia auctor. Donec a libero fermentum quam eleifend tempus in in tortor.</p>
  <div class="who"><b>Corin Vale.</b>Sed a euismod tur</div>
  <div class="av" role="img" aria-label="Portrait photo of the client"></div>
</div>
<div class="abs tcard" style="left:602px">
  <div class="q">❝</div>
  <p>Sed a euismod turpis. Donec ullamcorper digni ssim suscipit. Quisque libero tortor, tempus et egestas sit amet, porttitor et dolor. Aenean ultri cies imperdiet velit ut finibus. Suspendisse sit amet massa orci. Morbi pellentesque eros quis lacinia auctor. Donec a libero fermentum quam eleifend tempus in in tortor.</p>
  <div class="who"><b>Corin Vale.</b>Sed a euismod tur</div>
  <div class="av" role="img" aria-label="Portrait photo of the client" style="background:linear-gradient(160deg,#b77a5a,#4a2a22)"></div>
</div>
<svg class="abs" style="left:550px;top:3032px" width="100" height="38" viewBox="0 0 100 38"><circle cx="35" cy="19" r="18" fill="none" stroke="#0f1a3d"/><circle cx="65" cy="19" r="18" fill="none" stroke="#0f1a3d"/><path d="M2 19h40M8 13l-6 6 6 6M58 19h40M92 13l6 6-6 6" stroke="#5fbcc2" fill="none" stroke-width="1.4"/></svg>

<section class="abs blogs">
  <div class="abs center kicker c" style="top:72px">BLOGS</div>
  <h2 class="abs center sec-title" style="top:96px">Our <b>Latest</b><br><b>Blogs</b></h2>
  <div class="abs bcard" style="left:150px">
    <div class="pic" role="img" aria-label="Photo of a distressed man in a group therapy circle" style="background:linear-gradient(170deg,#e4e2df,#9b9a9a 55%,#5d6476)"></div>
    <div class="plus"><svg width="30" height="30" viewBox="0 0 16 16"><path d="M8 1v5M8 10v5M1 8h5M10 8h5" stroke="#fff" stroke-width="3" stroke-linecap="round"/></svg></div>
    <h3>Is It Important to Say “Please”<br>and “Thank You” to Your Partner?</h3>
  </div>
  <div class="abs bcard" style="left:456px">
    <div class="pic" role="img" aria-label="Photo of a pensive woman hugging her knees on a chair" style="background:linear-gradient(170deg,#d6d1c8,#9a8f7f 55%,#6a6550)"></div>
    <div class="plus"><svg width="30" height="30" viewBox="0 0 16 16"><path d="M8 1v5M8 10v5M1 8h5M10 8h5" stroke="#fff" stroke-width="3" stroke-linecap="round"/></svg></div>
    <h3>Is It Important to Say “Please”<br>and “Thank You” to Your Partner?</h3>
  </div>
  <div class="abs bcard" style="left:760px">
    <div class="pic" role="img" aria-label="Photo of a man talking with a counsellor in a bright office" style="background:linear-gradient(170deg,#efece6,#c7bba9 55%,#8a8478)"></div>
    <div class="plus"><svg width="30" height="30" viewBox="0 0 16 16"><path d="M8 1v5M8 10v5M1 8h5M10 8h5" stroke="#fff" stroke-width="3" stroke-linecap="round"/></svg></div>
    <h3>Is It Important to Say “Please”<br>and “Thank You” to Your Partner?</h3>
  </div>
</section>
<svg class="abs tear" style="top:3810px" width="1200" height="24" viewBox="0 0 1200 24" preserveAspectRatio="none"><path d="M0 10 L60 4 L130 13 L200 5 L270 12 L340 4 L410 13 L480 6 L550 12 L620 4 L690 13 L760 6 L830 12 L900 4 L970 12 L1040 5 L1110 13 L1200 6 L1200 24 L0 24Z" fill="#fff"/></svg>

<h2 class="abs center sec-title" style="top:3888px">Our <b>Partners</b></h2>
<div class="abs plogo" style="left:155px"><span></span></div>
<div class="abs plogo" style="left:334px"><span></span></div>
<div class="abs plogo" style="left:513px"><span></span></div>
<div class="abs plogo" style="left:692px"><span></span></div>
<div class="abs plogo" style="left:871px"><span></span></div>

<footer class="abs footer">
  <div class="abs brand2">Elmwood Health</div>
  <p class="abs about-txt">Aenean ultricies imperdiet velit ut finibus. Suspendisse sit amet massa orci. Morbi pell entesque eros quis lacinia auctor. Donec a libero fermentum quam eleifend tempus in in tortor. Nunc finibus fringilla efficitur.</p>
  <h4 class="abs" style="left:533px;top:54px">QUICK LINKS</h4>
  <ul class="abs links" style="left:533px;top:106px">
    <li><span class="caret">➤</span>Home</li><li><span class="caret">➤</span>About</li><li><span class="caret">➤</span>Services</li><li><span class="caret">➤</span>News &amp; Events</li><li><span class="caret">➤</span>Contact</li>
  </ul>
  <h4 class="abs" style="left:779px;top:54px">CONTACT INFO</h4>
  <ul class="abs contact" style="left:779px;top:106px;width:260px">
    <li><span class="caret">➤</span><span>Information in accordance with § 5 TMG: Tarnvale GmbH Lindqvist Weg 4c 13281 Halden</span></li>
    <li><span class="caret">➤</span>Toll Free: +49 (030) 71 44 60 12</li>
    <li><span class="caret">➤</span>Fax: +49 (030) 71 44 60 13</li>
    <li><span class="caret">➤</span>Email: elmwoodmind-gmbh@mailvale.de</li>
  </ul>
  <div class="abs copy">Copyright © 2025 Elmwood Health Services. All rights reserved.</div>
</footer>

</body>
</html>
```